Korvane Sky Works, LLC - Business Card

I currently have a drone business that specializes in aerial photography, thermal image inspections, deer recovery, search and rescue, custom agricultural applications. i will attach my current business card as well as some logos to incorporate for a new up to date business card
Updates

Designs look the same

Sick

Target Market(s)

farmers, hunters

Contact Information for Business Card

name address phone number (as existing card i attached)

Requirements
Must have
• im good with existing business card, but would like an agricultural twist

```html
<!DOCTYPE html>
<html lang="en">
<head>
<meta charset="utf-8">
<title>Korvane Sky Works, LLC – Business Card</title>
<link href="https://fonts.googleapis.com/css2?family=Archivo:wght@500;600;700;800&display=swap" rel="stylesheet">
<style>
  :root {
    --backdrop: #a8a8a8;
    --card: #ffffff;
    --ink: #1c1c1c;
    --ink-soft: #333333;
    --green: #3a8d1e;
  }
  * { margin: 0; padding: 0; box-sizing: border-box; }
  html, body {
    width: 764px; height: 1200px; overflow: hidden;
    background: var(--backdrop);
    font-family: "Archivo", Arial, sans-serif;
  }
  .card {
    position: absolute; left: 82px; width: 600px; height: 396px;
    background: var(--card);
  }
  .card--front { top: 136px; }
  .card--back { top: 668px; }

  .brand-mark {
    position: absolute; left: 48px; top: 94px;
    display: flex; align-items: center; gap: 8px;
    font-weight: 800; font-size: 26px; color: var(--green);
    letter-spacing: 0.5px;
  }
  .brand-dot { width: 14px; height: 14px; border-radius: 50%; background: var(--green); }

  .holder { position: absolute; left: 286px; top: 82px; }
  .holder-name { font-weight: 800; font-size: 31px; color: var(--ink); letter-spacing: 0.3px; line-height: 1; }
  .holder-role { margin-top: 9px; font-weight: 700; font-size: 17px; color: var(--green); line-height: 1; }

  .services { position: absolute; left: 50px; top: 164px; list-style: none; }
  .services::before {
    content: ""; position: absolute; left: 4px; top: 12px; width: 1.5px; height: 134px; background: var(--green);
  }
  .services li {
    position: relative; height: 45px; padding-left: 20px;
    font-weight: 600; font-size: 15px; color: var(--ink-soft); line-height: 22px;
  }
  .services li::before {
    content: ""; position: absolute; left: 2px; top: 9px; width: 5px; height: 5px; background: var(--green);
  }

  .contacts { position: absolute; left: 286px; top: 163px; list-style: none; }
  .contacts li {
    display: flex; align-items: center; gap: 14px; height: 45px;
    font-weight: 600; font-size: 15px; color: var(--ink-soft);
  }
  .contact-icon {
    width: 25px; height: 25px; border-radius: 50%; background: var(--green);
    display: flex; align-items: center; justify-content: center; flex: none;
  }
  .contact-icon svg { width: 14px; height: 14px; }

  .back-mark {
    position: absolute; left: 0; right: 0; top: 174px;
    display: flex; align-items: center; justify-content: center; gap: 10px;
    font-weight: 800; font-size: 34px; color: var(--green); letter-spacing: 0.5px;
  }
  .back-mark .brand-dot { width: 18px; height: 18px; }
</style>
</head>
<body>
  <section class="card card--front">
    <div class="brand-mark"><span class="brand-dot"></span>Korvane</div>

    <div class="holder">
      <h1 class="holder-name">DORIAN HALVEY</h1>
      <p class="holder-role">OWNER</p>
    </div>

    <ul class="services">
      <li>thermal Image inspections</li>
      <li>deer recovery</li>
      <li>search &amp; rescue</li>
      <li>real estate potography</li>
    </ul>

    <ul class="contacts">
      <li>
        <span class="contact-icon"><svg viewBox="0 0 24 24"><path fill="#fff" d="M6.6 10.8a15 15 0 0 0 6.6 6.6l2.2-2.2c.3-.3.7-.4 1-.2 1.1.4 2.3.6 3.6.6.6 0 1 .4 1 1V20c0 .6-.4 1-1 1A17 17 0 0 1 3 4c0-.6.4-1 1-1h3.5c.6 0 1 .4 1 1 0 1.3.2 2.5.6 3.6.1.3 0 .7-.2 1z"/></svg></span>
        555-014-2286
      </li>
      <li>
        <span class="contact-icon"><svg viewBox="0 0 24 24" fill="none" stroke="#fff" stroke-width="1.8"><circle cx="12" cy="12" r="9"/><path d="M3 12h18M12 3c2.5 2.5 3.5 5.5 3.5 9s-1 6.5-3.5 9c-2.5-2.5-3.5-5.5-3.5-9s1-6.5 3.5-9z"/></svg></span>
        www.korvaneskyworks.com
      </li>
      <li>
        <span class="contact-icon"><svg viewBox="0 0 24 24" fill="none" stroke="#fff" stroke-width="1.8"><rect x="3" y="6" width="18" height="12" rx="1"/><path d="M3 6l9 7 9-7"/></svg></span>
        korvaneskyworks@mail.com
      </li>
      <li>
        <span class="contact-icon"><svg viewBox="0 0 24 24"><path fill="#fff" d="M12 2a7 7 0 0 0-7 7c0 5 7 13 7 13s7-8 7-13a7 7 0 0 0-7-7zm0 9.5A2.5 2.5 0 1 1 12 6.5a2.5 2.5 0 0 1 0 5z"/></svg></span>
        214 W. Orchard Rd. Dalemont, OH 45000
      </li>
    </ul>
  </section>

  <section class="card card--back">
    <div class="back-mark"><span class="brand-dot"></span>Korvane</div>
  </section>
</body>
</html>
```